Thornwell Building Company - advertisement poster

I am looking to print some canvas signs to advertise my general contracting company, Thornwell Building Company. The sign will measure 6' long x 3' high so the size should match that ratio. I already have a logo icon, which is the Letter 'A' and some trees that I would like to incorporate, see attached. I would also like the to have the following information listed:
1) phone number: 472-318-6095
2) email: thornwellbuildingcompany@mailvistra.net
3) website: thornwellbuildingcompany.com
4) Lic#5386204
5) I want to use this text: "BUILD WITH THE T-CREW!"

The ad should be relatively simple and clean. Black and Green are my company colors. I am open to creative ideas!

Target Market(s)

People looking to renovate their homes

Industry/Entity Type

Construction

Colors
59FF00
82FF00
B8FF75
E3FFCB
F4FFEA

Requirements
Must have
• Must have my company logo
Should not have
• No photos or complex graphics

```html
<!DOCTYPE html>
<html lang="en">
<head>
<meta charset="utf-8">
<title>Thornwell Building Company – Canvas Sign</title>
<link href="https://fonts.googleapis.com/css2?family=Bebas+Neue&family=Montserrat:wght@500;700;800&display=swap" rel="stylesheet">
<style>
  :root {
    --page: #d9d9d9;
    --charcoal: #2f2e31;
    --charcoal-light: #3a393c;
    --charcoal-line: #262528;
    --green: #6db344;
    --white: #ffffff;
  }
  html, body {
    margin: 0;
    width: 1200px;
    height: 640px;
    overflow: hidden;
    background: var(--page);
  }
  .sign {
    position: absolute;
    left: 10px;
    top: 25px;
    width: 1180px;
    height: 590px;
    background: var(--charcoal);
    overflow: hidden;
    font-family: "Montserrat", Arial, sans-serif;
    color: var(--white);
  }
  .sign__backdrop {
    position: absolute;
    inset: 0;
  }
  .headline {
    position: absolute;
    left: 58px;
    top: 48px;
    margin: 0;
    font-family: "Bebas Neue", "Oswald", sans-serif;
    font-weight: 400;
    font-size: 150px;
    line-height: 134px;
    letter-spacing: 1px;
    text-shadow: 4px 4px 0 rgba(0,0,0,0.35);
  }
  .headline__accent { color: var(--green); }

  .license-tab {
    position: absolute;
    right: 0;
    top: 0;
    width: 352px;
    height: 78px;
  }
  .license-tab__text {
    position: absolute;
    right: 32px;
    top: 21px;
    font-weight: 800;
    font-size: 27px;
    letter-spacing: 1.5px;
  }

  .brand {
    position: absolute;
    left: 560px;
    width: 578px;
    top: 100px;
    text-align: center;
  }
  .brand__mark {
    width: 120px;
    height: 120px;
    margin: 0 auto;
    background: var(--green);
  }
  .brand__est {
    position: absolute;
    top: 90px;
    width: 92px;
    border-top: 2px solid var(--green);
    border-bottom: 2px solid var(--green);
    padding: 5px 0;
    font-weight: 500;
    font-size: 16px;
    letter-spacing: 4px;
  }
  .brand__est--left { left: 26px; }
  .brand__est--right { right: 26px; }
  .brand__name {
    margin: 22px 0 0;
    font-weight: 800;
    font-size: 56px;
    line-height: 58px;
    letter-spacing: 1px;
    color: var(--white);
  }
  .brand__sub {
    display: block;
    font-size: 27px;
    line-height: 36px;
    letter-spacing: 7px;
  }

  .phone {
    position: absolute;
    left: 568px;
    top: 413px;
    width: 562px;
    height: 60px;
  }
  .phone__bar {
    position: absolute;
    left: 30px;
    right: 0;
    top: 2px;
    bottom: 2px;
    background: var(--green);
    border-radius: 28px;
  }
  .phone__icon {
    position: absolute;
    left: 0;
    top: 0;
    width: 60px;
    height: 60px;
    border-radius: 50%;
    background: var(--white);
    border: 3px solid var(--charcoal);
    box-sizing: border-box;
  }
  .phone__number {
    position: absolute;
    left: 78px;
    top: 6px;
    font-weight: 800;
    font-size: 40px;
    letter-spacing: 2px;
  }

  .footer__text {
    position: absolute;
    top: 528px;
    font-weight: 500;
    font-size: 19px;
  }
  .footer__email { left: 54px; }
  .footer__web { right: 56px; }
</style>
</head>
<body>
<main class="sign">
  <svg class="sign__backdrop" width="1180" height="590" viewBox="0 0 1180 590" aria-hidden="true">
    <polygon points="0,520 470,0 0,0" fill="var(--charcoal)"/>
    <polygon points="0,512 470,0 640,0 240,512" fill="var(--charcoal-light)" opacity="0.35"/>
    <polyline points="538,512 538,150 848,-40 1150,150 1150,512" fill="none" stroke="var(--charcoal-line)" stroke-width="14"/>
    <polyline points="760,0 848,-60 980,0" fill="none" stroke="var(--charcoal-line)" stroke-width="14"/>
    <polygon points="0,512 545,512 592,583 650,512 1180,512 1180,590 0,590" fill="var(--green)"/>
    <polyline points="545,528 592,585 640,528" fill="none" stroke="var(--white)" stroke-width="6" stroke-linejoin="miter"/>
  </svg>

  <h1 class="headline">BUILD<br>WITH THE<br><span class="headline__accent">T-CREW!</span></h1>

  <div class="license-tab">
    <svg width="352" height="78" viewBox="0 0 352 78" aria-hidden="true">
      <polygon points="0,0 352,0 352,78 78,78" fill="var(--green)"/>
    </svg>
    <span class="license-tab__text">Lic#5386204</span>
  </div>

  <div class="brand">
    <div class="brand__mark"></div>
    <span class="brand__est brand__est--left">ESTD</span>
    <span class="brand__est brand__est--right">2020</span>
    <p class="brand__name">THORNWELL<span class="brand__sub">BUILDING COMPANY</span></p>
  </div>

  <div class="phone">
    <div class="phone__bar"></div>
    <div class="phone__icon">
      <svg width="54" height="54" viewBox="0 0 54 54" aria-hidden="true">
        <path d="M19 15c1.5-1 3-.5 3.8 1l2.2 4.2c.6 1.2.3 2.5-.7 3.3l-1.6 1.3c1.3 2.8 3.4 5 6.2 6.4l1.3-1.6c.8-1 2.2-1.3 3.4-.7l4.2 2.2c1.5.8 2 2.4 1 3.8l-1.6 2.2c-1 1.4-2.8 2-4.5 1.5C24.5 36.7 17.4 29.6 15.5 21.4c-.4-1.7.2-3.5 1.6-4.5z" fill="none" stroke="var(--green)" stroke-width="2.2" stroke-linejoin="round"/>
        <path d="M30 14a10 10 0 0 1 10 10M30 19a5 5 0 0 1 5 5" fill="none" stroke="var(--green)" stroke-width="2.2" stroke-linecap="round"/>
      </svg>
    </div>
    <span class="phone__number">472-318-6095</span>
  </div>

  <span class="footer__text footer__email">thornwellbuildingcompany@mailvistra.net</span>
  <span class="footer__text footer__web">www.ThornwellBuildingCompany.com</span>
</main>
</body>
</html>
```